Website design to promote trampoline business

We require a website design for our business. The business is primarily provising access for people between 5YO and 40YO to jump on trampolines for fun and fitness.

We have a logo and color schemes already and the website should incorporate these colors and designs.

We would like to incorporate the following pages:-

Book Now!
Home
About Us
Locations & Hours
Jumping
Groups & Events
Gallery
Safety
Latest News
Careers

Industry/Entity Type

Business

Requirements
Must have
• Incorporate our logo and colors (files attached).

```html
<!DOCTYPE html>
<html lang="en">
<head>
<meta charset="utf-8">
<title>Bounce Loft – Home</title>
<link rel="stylesheet" href="https://fonts.googleapis.com/css2?family=Roboto:wght@300;400;500;700&display=swap">
<style>
:root{
  --orange:#ff7f00;
  --blue:#27a9d1;
  --page:#f4f4f4;
  --card:#ffffff;
  --ink:#333333;
  --muted:#666666;
  --stage:#ececec;
  --photo-green:#7fa35a;
  --photo-sky:#c8dcc0;
}
*{box-sizing:border-box;margin:0;padding:0}
html,body{width:1200px;height:1000px;overflow:hidden}
body{background:var(--stage);font-family:'Roboto',sans-serif;color:var(--ink);position:relative}
.page{position:absolute;left:326px;top:32px;width:548px;height:936px;background:var(--page);border:1px solid #dcdcdc}
.page > *{position:absolute}
.brand{left:62px;top:26px;display:flex;align-items:center;gap:6px;color:var(--orange);font-weight:700;font-size:17px;letter-spacing:.5px}
.brand-mark{width:12px;height:12px;background:var(--orange)}
.book-now{right:38px;top:32px;color:var(--orange);font-weight:700;font-size:10px}
.nav{left:58px;top:67px;height:53px;width:440px;display:flex}
.nav-item{display:flex;flex-direction:column;align-items:center;justify-content:center;gap:4px;font-size:11px;color:var(--ink);height:100%}
.nav-item svg{width:18px;height:18px;fill:none;stroke:var(--blue);stroke-width:1.4}
.nav-item.active{background:var(--orange);color:#fff;width:43px}
.nav-item.active svg{stroke:#fff}
.hero{left:52px;top:126px;width:453px;height:279px;display:flex}
.photo{background:linear-gradient(180deg,var(--photo-sky),var(--photo-green) 60%,#3c4f6e)}
.hero .photo{width:188px;height:100%}
.hero-panel{flex:1;background:var(--orange);color:#fff;position:relative;padding:66px 22px 0 22px}
.hero-title{font-weight:300;font-size:25px;line-height:27px}
.hero-text{font-size:7.5px;line-height:11px;margin-top:14px;font-weight:300}
.btn{position:absolute;display:flex;align-items:center;justify-content:center;width:63px;height:20px;font-size:9px;color:#fff}
.btn-blue{background:var(--blue)}
.btn-orange{background:var(--orange)}
.hero-panel .btn{left:172px;top:226px}
.dots{position:absolute;left:12px;top:255px;display:flex;gap:10px}
.dots span{width:8px;height:8px;border-radius:50%;background:#fff}
.dots span.on{background:var(--blue)}
.card{background:var(--card)}
.card .btn{position:absolute}
.card-title{position:absolute;font-weight:300;font-size:26px;color:#444}
.card-text{position:absolute;font-size:7.5px;line-height:10.5px;color:var(--muted)}
.about{left:47px;top:420px;width:180px;height:183px}
.safety{left:240px;top:420px;width:265px;height:183px}
.safety .photo{position:absolute;right:0;top:0;width:124px;height:183px}
.small-title{position:absolute;left:14px;top:15px;font-size:11px;color:#555}
.gallery{left:47px;top:614px;width:146px;height:213px}
.thumbs{position:absolute;left:19px;top:42px;display:grid;grid-template-columns:repeat(4,24px);grid-auto-rows:32px;gap:5px 3px}
.thumbs .photo{width:24px;height:32px}
.groups{left:203px;top:614px;width:146px;height:213px}
.groups .photo{position:absolute;left:12px;top:34px;width:121px;height:56px}
.news{left:359px;top:614px;width:146px;height:213px}
.news-date{position:absolute;right:12px;font-size:8px;font-style:italic;color:var(--orange)}
.news .photo{position:absolute;left:4px;width:34px;height:33px}
.news .card-text{left:43px;width:98px}
.footer{left:47px;top:847px;width:458px;height:26px;display:flex}
.social{width:103px;background:var(--orange);display:flex;align-items:center;gap:4px;padding-left:12px}
.social span{width:14px;height:14px;background:#fff;opacity:.85}
.footer-links{flex:1;background:var(--blue);color:#fff;font-size:8px;display:flex;align-items:center;justify-content:flex-end;padding-right:14px;gap:5px}
.copyright{left:0;width:100%;top:908px;text-align:center;font-size:8px;color:#888}
</style>
</head>
<body>
<div class="page">
  <div class="brand"><span class="brand-mark"></span>BOUNCE LOFT</div>
  <div class="book-now">BOOK NOW !! +0100 55555</div>

  <nav class="nav">
    <div class="nav-item active"><svg viewBox="0 0 20 20"><path d="M3 10 L10 3 L17 10 M5 8 V17 H15 V8"/></svg>Home</div>
    <div class="nav-item" style="width:70px"><svg viewBox="0 0 20 20"><circle cx="8" cy="8" r="5"/><path d="M12 12 L17 17"/></svg>About Us</div>
    <div class="nav-item" style="width:106px"><svg viewBox="0 0 20 20"><path d="M7 3 L14 5 L11 10 L8 9 Z M9 9 L6 17"/></svg>Locations &amp; Hours</div>
    <div class="nav-item" style="width:78px"><svg viewBox="0 0 20 20"><path d="M5 17 V8 Q5 4 9 4 Q13 4 13 8 V17 M13 8 Q13 4 16 5"/></svg>Jumping</div>
    <div class="nav-item" style="width:74px"><svg viewBox="0 0 20 20"><rect x="5" y="9" width="10" height="8" rx="1"/><path d="M7 9 V6 Q10 2 13 6 V9"/></svg>Safety</div>
    <div class="nav-item" style="width:66px"><svg viewBox="0 0 20 20"><rect x="5" y="3" width="10" height="14" rx="2"/><path d="M4 7 H6 M4 10 H6 M4 13 H6"/></svg>Careers</div>
  </nav>

  <section class="hero">
    <div class="photo" role="img" aria-label="Photo of a couple jumping on a garden trampoline"></div>
    <div class="hero-panel">
      <h1 class="hero-title">We believe that '<br>quality' is an ongoing<br>commitment.</h1>
      <p class="hero-text">Lorem ipsum dolor sit amet, consectetur adipiscing elit. Nunc viverra rutrum est, non faucibus mi congue id. Integer accumsan tempor tristique. Maecenas nunc sem, dignissim quis lacus</p>
      <a class="btn btn-blue">Read More //</a>
      <div class="dots"><span></span><span></span><span></span><span class="on"></span></div>
    </div>
  </section>

  <section class="card about">
    <h2 class="card-title" style="left:26px;top:8px">About us</h2>
    <p class="card-text" style="left:28px;top:54px;width:128px">Lorem ipsum dolor sit amet, consectetur adipiscing elit. Nunc viverra rutrum est, non faucibus mi congue id. Integer accumsan tempor tristique. Maecenas nunc sem, dignissim quis lacus ornare, venenatis sodales lorem. Class aptent taciti sociosqu ad litora torquent per</p>
    <a class="btn btn-orange" style="left:96px;top:150px">Read More //</a>
  </section>

  <section class="card safety">
    <h2 class="card-title" style="left:16px;top:8px">Safety</h2>
    <p class="card-text" style="left:16px;top:54px;width:104px">Lorem ipsum dolor sit amet, consectetur adipiscing elit. Nunc viverra rutrum est, non faucibus mi congue id. Integer accumsan tempor tristique. Maecenas nunc sem, dignissim quis lacus ornare, venena-</p>
    <a class="btn btn-orange" style="left:61px;top:150px">Read More //</a>
    <div class="photo" role="img" aria-label="Photo of a smiling couple sitting together outdoors"></div>
  </section>

  <section class="card gallery">
    <h3 class="small-title">Gallery</h3>
    <div class="thumbs" role="img" aria-label="Grid of gallery thumbnail photos">
      <div class="photo"></div><div class="photo"></div><div class="photo"></div><div class="photo"></div>
      <div class="photo"></div><div class="photo"></div><div class="photo"></div><div class="photo"></div>
      <div class="photo"></div><div class="photo"></div><div class="photo"></div><div class="photo"></div>
    </div>
    <a class="btn btn-blue" style="left:63px;top:174px">Read More //</a>
  </section>

  <section class="card groups">
    <h3 class="small-title" style="left:12px">Groups &amp; Events</h3>
    <div class="photo" role="img" aria-label="Photo of a couple jumping together"></div>
    <p class="card-text" style="left:12px;top:100px;width:124px">Lorem ipsum dolor sit amet, consectetur adipiscing elit. Nunc viverra rutrum est, non faucibus mi congue id. Integer accumsan tempor tristique. Maecenas nunc sem, dignissim quis lacus ornare,</p>
    <a class="btn btn-blue" style="left:69px;top:174px">Read More //</a>
  </section>

  <section class="card news">
    <h3 class="small-title" style="left:10px">News</h3>
    <span class="news-date" style="top:31px">13/05/2014</span>
    <div class="photo" style="top:42px" role="img" aria-label="News thumbnail photo"></div>
    <p class="card-text" style="top:44px">Lorem ipsum dolor sit amet, consectetur adipiscing elit. Nunc viverra rutrum est, non</p>
    <a class="btn btn-blue" style="left:68px;top:86px">Read More //</a>
    <span class="news-date" style="top:121px">13/05/2014</span>
    <div class="photo" style="top:132px" role="img" aria-label="News thumbnail photo"></div>
    <p class="card-text" style="top:134px">Lorem ipsum dolor sit amet, consectetur adipiscing elit. Nunc viverra rutrum est, non</p>
    <a class="btn btn-blue" style="left:68px;top:175px">Read More //</a>
  </section>

  <footer class="footer">
    <div class="social"><span></span><span></span><span></span><span></span></div>
    <div class="footer-links">Privacy Policy <span>|</span> FAQ <span>|</span> Contact Us</div>
  </footer>
  <p class="copyright">© 2012-2015 BOUNCE LOFT. All Rights Reserved.</p>
</div>
</body>
</html>
```